Existing graphics (3D cube) should be made more understandable

Hi,
I would like to make my 3D cube more understandable, but it should also be more presentable. I have attached a detailed description as an attachment. I think the image so far is good, but if we can improve it (more understandable and prettier), I would be happy.
BR
Rob

Target Market(s)

Students, Teachers, Prof.

Colors
0054AA
0677BA
7BADD7
CADEEF
E8F1F8
0094D4
00A9DD
6FCCEA
C7EBF8
E9F6FB
00AB8E
00BBA5
67D7C9
C6EFE9
E9F9F6
59FF00
82FF00
B8FF75
E3FFCB
F4FFEA

Requirements
Must have
• please see attachment
Nice to have
• please see attachment
Should not have
• please see attachment

```html
<!DOCTYPE html>
<html lang="de">
<head>
<meta charset="utf-8">
<title>Führungskräfte-Würfel</title>
<link href="https://fonts.googleapis.com/css2?family=Roboto:ital,wght@0,500;0,700;0,900;1,900&display=swap" rel="stylesheet">
<style>
  :root{
    --bg:#ffffff;
    --ink:#111111;
    --axis:#5aafc0;
    --scale-blue:#2a56a8;
    --teal:#18a596;
    --face-front:#b3bfe2;
    --face-front-light:#c2cbe8;
    --face-front-dark:#97abdb;
    --face-top:#adb9de;
    --face-top-light:#bcc5e4;
    --face-side:#a9b5dd;
    --face-side-light:#c5cbe6;
    --thumb-dark:#3a3a3a;
  }
  html,body{margin:0;padding:0;overflow:hidden;background:var(--bg);}
  .canvas{position:relative;width:1200px;height:1200px;overflow:hidden;font-family:"Roboto",Arial,sans-serif;}
  .canvas svg{position:absolute;left:0;top:0;}
  .label{font-family:"Roboto",Arial,sans-serif;font-weight:700;fill:var(--ink);text-anchor:middle;}
  .axis-label{font-size:25px;}
  .cell-title{font-size:27px;font-weight:900;}
  .cell-body{font-size:23.5px;}
  .cell-top{font-size:21px;font-weight:900;font-style:italic;}
  .scale{font-family:"Roboto",Arial,sans-serif;font-weight:700;fill:var(--scale-blue);font-size:30px;text-anchor:middle;}
  .scale-end{font-size:34px;font-weight:900;}
  .note{font-family:"Roboto",Arial,sans-serif;font-weight:700;fill:var(--teal);font-size:24px;text-anchor:middle;}
  .app-name{font-family:"Roboto",Arial,sans-serif;font-weight:700;fill:#ffffff;font-size:13px;text-anchor:middle;}
</style>
</head>
<body>
<div class="canvas">
<svg width="1200" height="1200" viewBox="0 0 1200 1200" xmlns="http://www.w3.org/2000/svg">

  <!-- side notes -->
  <g class="side-notes">
    <text class="note" x="115" y="60">open fonts</text>
    <text class="note" x="115" y="83">for further edition</text>
    <rect x="12" y="86" width="194" height="190" fill="#f2f3f7" role="img" aria-label="Kleine Vorschau der editierbaren Diagrammdatei"/>
    <rect x="13" y="92" width="58" height="60" fill="#2b2b33"/>
    <text class="app-name" x="42" y="127">Vectra</text>
    <rect x="71" y="92" width="56" height="60" fill="#c9303a"/>
    <text class="app-name" x="99" y="127">Docu</text>
    <text class="note" x="110" y="304">unique 3d made</text>
    <text class="note" x="110" y="327">graphics</text>
    <rect x="5" y="334" width="201" height="200" fill="#a9b0d8" role="img" aria-label="Vorschau des 3D-Würfelmodells im Modellierungsprogramm"/>
    <rect x="5" y="334" width="62" height="62" fill="var(--thumb-dark)"/>
    <text class="app-name" x="36" y="370">Mesh3</text>
  </g>

  <!-- cube -->
  <g class="cube">
    <!-- right side faces -->
    <polygon points="779,587 979,382 979,581 779,781" fill="var(--face-side-light)"/>
    <polygon points="779,781 979,581 979,773 779,978" fill="var(--face-side)"/>
    <!-- top faces -->
    <polygon points="386,587 587,382 779,382 584,587" fill="var(--face-top)"/>
    <polygon points="584,587 779,382 979,382 779,587" fill="var(--face-top-light)"/>
    <!-- front faces -->
    <rect x="386" y="587" width="198" height="194" rx="4" fill="var(--face-front)"/>
    <rect x="584" y="587" width="195" height="194" rx="4" fill="var(--face-front-light)"/>
    <rect x="386" y="781" width="198" height="197" rx="4" fill="var(--face-front-dark)"/>
    <rect x="584" y="781" width="195" height="197" rx="4" fill="var(--face-front)"/>
    <g stroke="#9aa8d6" stroke-width="1.5" fill="none">
      <line x1="584" y1="587" x2="584" y2="978"/>
      <line x1="386" y1="781" x2="779" y2="781"/>
      <line x1="584" y1="587" x2="779" y2="382"/>
      <line x1="779" y1="781" x2="979" y2="581"/>
    </g>
  </g>

  <!-- axes -->
  <g class="axes" fill="var(--axis)" stroke="var(--axis)">
    <line x1="368" y1="997" x2="368" y2="480" stroke-width="7"/>
    <polygon points="368,467 349,490 387,490" stroke="none"/>
    <line x1="365" y1="997" x2="835" y2="997" stroke-width="7"/>
    <polygon points="852,997 830,978 830,1016" stroke="none"/>
    <line x1="373" y1="990" x2="995" y2="365" stroke-width="7"/>
    <polygon points="1008,352 980,358 1002,380" stroke="none"/>
  </g>

  <!-- cell labels -->
  <g class="cells">
    <text class="label cell-title" x="484" y="645">Kategorie I:</text>
    <text class="label cell-body" x="484" y="674">Führungskraft</text>
    <text class="label cell-body" x="484" y="703">fürs</text>
    <text class="label cell-body" x="484" y="732">Leadership</text>
    <text class="label cell-body" x="484" y="761">(L)</text>

    <text class="label cell-title" x="681" y="645">Kategorie II:</text>
    <text class="label cell-body" x="681" y="674">Führungskraft</text>
    <text class="label cell-body" x="681" y="703">fürs Leadership</text>
    <text class="label cell-body" x="681" y="732">und Management</text>
    <text class="label cell-body" x="681" y="761">(LM)</text>

    <text class="label cell-title" x="484" y="828">Kategorie V:</text>
    <text class="label cell-body" x="484" y="855">Weder fürs</text>
    <text class="label cell-body" x="484" y="880">Management</text>
    <text class="label cell-body" x="484" y="905">noch Leadership</text>
    <text class="label cell-body" x="484" y="930">geeignet</text>
    <text class="label cell-body" x="484" y="956">(N)</text>

    <text class="label cell-title" x="681" y="834">Kategorie IV:</text>
    <text class="label cell-body" x="681" y="861">Führungskraft</text>
    <text class="label cell-body" x="681" y="890">fürs</text>
    <text class="label cell-body" x="681" y="920">Management</text>
    <text class="label cell-body" x="681" y="948">(M)</text>

    <text class="label cell-top" x="863" y="403">Kategorie III:</text>
    <text class="label cell-top" x="845" y="422">Führungskraft</text>
    <text class="label cell-top" x="826" y="441">fürs</text>
    <text class="label cell-top" x="807" y="460">Ambidextrous</text>
    <text class="label cell-top" x="789" y="479">Leadership (A)</text>
  </g>

  <!-- axis descriptions -->
  <g class="axis-descriptions">
    <text class="label axis-label" x="368" y="398">Exploration, Opening</text>
    <text class="label axis-label" x="368" y="429">Leadership, Leader-Rolle</text>

    <text class="label axis-label" x="1033" y="184">Flexibilität, um zwischen</text>
    <text class="label axis-label" x="1033" y="214">Exploration und Exploitation,</text>
    <text class="label axis-label" x="1033" y="245">Opening und Closing</text>
    <text class="label axis-label" x="1033" y="275">Leadership, Leader- und</text>
    <text class="label axis-label" x="1033" y="306">Manager-Rolle wechseln</text>
    <text class="label axis-label" x="1033" y="337">zu können</text>

    <text class="label axis-label" x="1020" y="981">Exploitation, Closing</text>
    <text class="label axis-label" x="1020" y="1012">Leadership, Manager-Rolle</text>
  </g>

  <!-- scales -->
  <g class="scales">
    <text class="scale" transform="translate(354,608) rotate(-90)">stark</text>
    <text class="scale" transform="translate(354,773) rotate(-90)">mittel</text>
    <text class="scale" transform="translate(354,932) rotate(-90)">schach</text>
    <text class="scale" x="435" y="1039">schach</text>
    <text class="scale" x="600" y="1039">mittel</text>
    <text class="scale" x="769" y="1039">stark</text>
    <text class="scale scale-end" transform="translate(312,1068) rotate(-45)">GERING</text>
    <text class="scale scale-end" transform="translate(1030,408) rotate(-45)">HOCH</text>
  </g>
</svg>
</div>
</body>
</html>
```